Stationery for London Estate Agents (Real Estate)

We are a modern and professional Estate Agency (Realtors) working with high quality properties in London.
We wish to redesign our stationary using our branding displayed on the front of our offices and require a digital version of this logo to be produced (photograph attached). Slight 'tweaking' of this branding is acceptable.
Updates
1st July 2010 Thank you all those designers who have uploaded submissions. Business Card - Details Side: Business Card - Logo Side: Outline of London Skyline Examples of the london skyline are available at http://www.pixorabank.example/searchkwy_london-skyline-silhouette Please be advised that we are looking for an outline, not a 'filled in' silhouette. Letterhead Please feel free to ask us any questions. Bertrand
I have been able to further refine our design requirements based on your submissions.
We like Blue Kettle' business card submission that has not been eliminated and have the following design clarifications;
a) Please use an email icon (e.g an envelope).
b) Please make the email as equally prominent as the telephone and fax
c) We very much like Fernwicky's 'mini window icon' - please display the website URL under such a mini window icon at the bottom right of the card.
We are very happy with the colouring, fonts and proportions used by Blue Kettle.
We invite designers to try adding an outline of the London Skyline to the left of the large window icon on the business card and in a suitablie position on the Letterhead (e.g at the top left of the letterhead).
We have the following design clarifiications to our Letterhead requirements;
A) We would like the main logo to be on the top right side of the letterhead.
B) We do NOT want the large window icon to be on the left of the logo or the bottom of the letterhead. We are happy having the large window icon to the right or underneath the TK brand.
C) Please use icons for tel, fax and email (e.g. envelope icon for e-mail address)
D) We like two coloured red borders, one at the top and bottom of the letterhead but are happy for variations in shape and size.
E) We currently prefer our address and contact details at the bottom of the letterhead.
F) We like Fernwicky's 'mini window icon' and would prefer this to be used to display the website URL at the bottom right of the letterhead.
G) Please be advised that the letterhead does NOT need additional space for the Company Name as per Blue Kettle' submission - the TK brand is sufficient.
Target Market(s)
Owners of high quality property in London.
Industry/Entity Type
Real Estate
Requirements
Must have
- Business Cards: We would like a 'vertical' style business card with our branding on one side and our staff's details on the other;
- Our website is www.tolkane.example and we are flexible where that should be on the card and letterhead.
- Stationery details are available in a file attached to this project.
Nice to have
- It would be great to have a horizontal version of the digital logo for placement on property portals (150x60)
Should not have
- Logo should not deviate significantly from the branding on our offices (shop front) - photograph attached.

```html
<!DOCTYPE html>
<html lang="en">
<head>
<meta charset="utf-8">
<title>Tolkane Residential – Letterhead &amp; Business Cards</title>
<link rel="stylesheet" href="https://fonts.googleapis.com/css2?family=Arimo:wght@400;700&display=swap">
<style>
  :root {
    --brand-red: #c4303f;
    --brand-yellow: #f9c85c;
    --paper: #ffffff;
    --backdrop: #e6cfb1;
    --ink: #111111;
    --white: #ffffff;
  }
  * { box-sizing: border-box; margin: 0; padding: 0; }
  html, body { width: 1200px; height: 899px; overflow: hidden; }
  body {
    position: relative;
    background: var(--backdrop);
    font-family: "Arimo", Arial, sans-serif;
    color: var(--ink);
  }

  .presentation-title {
    position: absolute;
    left: 800px;
    top: 55px;
    font-size: 39px;
    font-weight: 400;
    line-height: 1.2;
  }

  /* Letterhead */
  .letterhead {
    position: absolute;
    left: 120px;
    top: 36px;
    width: 590px;
    height: 830px;
    background: var(--paper);
  }
  .letterhead-brand {
    position: absolute;
    right: 32px;
    top: 30px;
    width: 148px;
    height: 148px;
    background: var(--brand-red);
    padding: 26px 16px 0;
  }
  .brand-name {
    color: var(--white);
    font-weight: 700;
    font-size: 17px;
    line-height: 1.2;
    text-align: center;
    letter-spacing: 0.3px;
  }
  .brand-square {
    display: block;
    width: 34px;
    height: 34px;
    background: var(--brand-yellow);
    margin: 20px auto 0;
  }
  .letterhead-contact {
    position: absolute;
    right: 42px;
    bottom: 52px;
    text-align: right;
    color: var(--brand-red);
    font-size: 10.5px;
    line-height: 1.3;
  }
  .letterhead-contact p + p { margin-top: 12px; }
  .contact-web { font-weight: 700; font-size: 11px; }
  .registration-line {
    position: absolute;
    right: 42px;
    bottom: 24px;
    color: var(--brand-red);
    font-size: 8px;
  }

  /* Business cards */
  .business-card {
    position: absolute;
    width: 152px;
    height: 228px;
    background: var(--brand-red);
    color: var(--white);
  }
  .card-front { left: 790px; top: 290px; padding: 28px 12px 0; }
  .card-front .brand-name { font-size: 16px; }
  .card-services {
    margin-top: 18px;
    text-align: center;
    font-weight: 700;
    font-size: 13px;
    line-height: 1.4;
  }
  .card-front .brand-square { width: 40px; height: 40px; margin-top: 24px; }

  .card-back { left: 972px; top: 318px; padding: 22px 14px 0; text-align: right; }
  .card-person { font-weight: 700; font-size: 12px; text-align: center; }
  .card-details { margin-top: 10px; font-size: 10px; line-height: 1.35; }
  .card-details + .card-details { margin-top: 10px; }
  .card-web {
    position: absolute;
    left: 0; right: 0;
    bottom: 18px;
    text-align: center;
    font-weight: 700;
    font-size: 11px;
  }
</style>
</head>
<body>

<h1 class="presentation-title">Letterhead &amp;<br>Business Cards</h1>

<section class="letterhead" aria-label="Letterhead">
  <div class="letterhead-brand">
    <p class="brand-name">TOLKANE<br>RESIDENTIAL</p>
    <span class="brand-square"></span>
  </div>

  <address class="letterhead-contact" style="font-style:normal">
    <p>24 Larkmoor Lane<br>Eastholm<br>London NW9 4QX</p>
    <p>t: 020 7946 0310<br>f: 020 7946 0322<br>m: 07700 900 418</p>
    <p>e: info@tolkane.example</p>
    <p class="contact-web">www.tolkane.example</p>
  </address>
  <p class="registration-line">Company registration details in one line at this point</p>
</section>

<section class="business-card card-front" aria-label="Business card, brand side">
  <p class="brand-name">TOLKANE<br>RESIDENTIAL</p>
  <p class="card-services">Lettings<br>Sales<br>Management<br>Investments</p>
  <span class="brand-square"></span>
</section>

<section class="business-card card-back" aria-label="Business card, details side">
  <p class="card-person">Bertrand Hale</p>
  <p class="card-details">24 Larkmoor Lane<br>Eastholm<br>London<br>NW9 4QX</p>
  <p class="card-details">t: 020 7946 0310<br>f: 020 7946 0322<br>m: 07700 900 418</p>
  <p class="card-details">e: bertrand@tolkane.example</p>
  <p class="card-web">www.tolkane.example</p>
</section>

</body>
</html>
```